Flyer YOga studio

I need a double sided DL flyer (landscape) with my yoga studio details on one side and my timetable on the back.

It looks like a lot of my info didn't save the orignal brief.

here is some information.

On the front side - Logo to be centred on white background.

Underneath text
$20 for 7 days unlimited yoga/pilates/run group
$99 for 1 month unlimited

also to be included - Location: Upstairs, 17 North Parade Linwood 3218
0438 915602
info@havenlinwood.com.au
www.havenlinwood.com.au

ON back side - Timetable only

Landscape

• Following text should be on front side

the logo
New clients offer: $20 for 7 days of Yoga
$99 - 1 month unlimited

Location: Upstairs, 17 North Parade
Linwood VIC 3218
info@havenlinwood.com.au/0438 915602

The following text:
Stretch...strength...Run
Any order you like...pick all or one. Only fear holds you back from experiencing any of these. We teach all our classes to what is happening in your body in this moment with an eye for alignment, correct muscle recruitment and breath awareness.

On the back:
Class descriptions:
Yoga: Flowing Vinyasa classes that heat the body through dynamic movements and slowing down for deep hip openers and relaxation.
Pilates: Mat classes for healthy bodies using a systematic sequencing of exercises that works the whole body, developing strength, flexibility and mindfulness.
Run groups: A non competitive session where you set the goals and we help you meet them, whether it getting to the corner and back or your first marathon.

```html
<!DOCTYPE html>
<html lang="en">
<head>
<meta charset="utf-8">
<title>Haven Yoga – DL Flyer Front</title>
<link rel="stylesheet" href="https://fonts.googleapis.com/css2?family=Open+Sans:wght@400;700&family=Montserrat:ital,wght@0,400;1,600&display=swap">
<style>
  :root {
    --stage: #6b6c6f;
    --paper: #f6f0e4;
    --paper-glow: #ffffff;
    --hill: #e3d5bb;
    --hill-deep: #c9b590;
    --ink: #4e3f28;
    --ink-soft: #5a4a30;
    --contact: #b6a482;
    --tagline: #8c7745;
    --body-copy: #bda986;
    --rule: #d8c9aa;
    --brand: #555558;
    --brand-dot: #f0a020;
  }
  * { margin: 0; padding: 0; box-sizing: border-box; }
  html, body { width: 1200px; height: 962px; overflow: hidden; }
  body {
    background: var(--stage);
    position: relative;
    font-family: "Open Sans", Arial, sans-serif;
  }
  .flyer {
    position: absolute;
    left: 53px; top: 219px;
    width: 1100px; height: 523px;
    overflow: hidden;
    background:
      radial-gradient(ellipse 420px 200px at 180px 110px, var(--paper-glow), transparent 70%),
      radial-gradient(ellipse 420px 200px at 920px 110px, var(--paper-glow), transparent 70%),
      var(--paper);
  }
  .flyer__hill { position: absolute; inset: 0; width: 1100px; height: 523px; }
  .contact-line {
    position: absolute; top: 22px;
    font-family: "Montserrat", Arial, sans-serif;
    font-size: 14.5px; letter-spacing: 4.1px;
    color: var(--contact);
  }
  .contact-line--email { left: 51px; }
  .contact-line--web { right: 68px; }
  .brand {
    position: absolute; left: 0; right: 0; top: 190px;
    display: flex; justify-content: center; align-items: center; gap: 14px;
    font-weight: 700; font-size: 36px; letter-spacing: 1px;
    color: var(--brand); text-transform: uppercase;
  }
  .brand__dot { width: 22px; height: 22px; border-radius: 50%; background: var(--brand-dot); }
  .offer {
    position: absolute; left: 229px; width: 300px; top: 302px;
    text-align: center; color: var(--ink); font-size: 20px; line-height: 27px;
  }
  .offer__line + .offer__line { margin-top: 9px; }
  .location {
    position: absolute; left: 594px; width: 300px; top: 302px;
    text-align: center; color: var(--ink-soft); font-size: 20px; line-height: 27px;
  }
  .location__phone {
    margin-top: 9px; font-weight: 700;
    display: flex; justify-content: center; align-items: center; gap: 6px;
  }
  .location__phone svg { width: 30px; height: 22px; }
  .divider { position: absolute; left: 407px; width: 330px; height: 1px; background: var(--rule); }
  .divider--top { top: 429px; }
  .divider--bottom { top: 457px; }
  .divider__flourish {
    position: absolute; left: 532px; top: 418px; width: 38px; height: 9px;
    background: var(--rule); border-radius: 4px;
  }
  .tagline {
    position: absolute; left: 0; right: 0; top: 435px;
    text-align: center;
    font-family: "Montserrat", Arial, sans-serif; font-style: italic; font-weight: 600;
    font-size: 13.5px; color: var(--tagline);
  }
  .philosophy {
    position: absolute; left: 90px; right: 90px; top: 463px;
    text-align: center;
    font-family: "Montserrat", Arial, sans-serif;
    font-size: 13.3px; line-height: 18px; color: var(--body-copy);
  }
</style>
</head>
<body>
  <section class="flyer" aria-label="Haven Yoga flyer front">
    <svg class="flyer__hill" viewBox="0 0 1100 523" aria-hidden="true">
      <defs>
        <radialGradient id="hillGlow" cx="550" cy="430" r="520" gradientUnits="userSpaceOnUse">
          <stop offset="0" stop-color="#ffffff"/>
          <stop offset="0.45" stop-color="#f3ebdc"/>
          <stop offset="1" stop-color="#cdb994"/>
        </radialGradient>
      </defs>
      <path d="M0 312 C 180 250, 380 238, 560 240 C 760 242, 960 250, 1100 268 L1100 523 L0 523 Z" fill="url(#hillGlow)"/>
    </svg>

    <p class="contact-line contact-line--email">info@havenlinwood.com.au</p>
    <p class="contact-line contact-line--web">www.havenlinwood.com.au</p>

    <div class="brand">
      <span class="brand__dot"></span>
      <span class="brand__name">Haven Yoga · Pilates · Fitness</span>
    </div>

    <div class="offer">
      <p class="offer__line"><b>$20</b> for <b>7 days</b> unlimited<br>yoga/pilates/run group</p>
      <p class="offer__line"><b>$99</b> for <b>1 month</b> unlimited</p>
    </div>

    <div class="location">
      <p>Upstairs, 17 North Parade<br>Linwood 3218</p>
      <p class="location__phone">
        <svg viewBox="0 0 30 22" aria-hidden="true">
          <path d="M6 4 C1 8 1 14 6 18" fill="none" stroke="#4e3f28" stroke-width="1.6"/>
          <path d="M12 3 L16 3 L17 7 L15 9 C16 12 18 14 21 15 L23 13 L27 14 L27 18 C20 19 11 12 12 3 Z" fill="#4e3f28"/>
        </svg>
        0438915602
      </p>
    </div>

    <div class="divider__flourish" role="img" aria-label="Small decorative flourish"></div>
    <div class="divider divider--top"></div>
    <p class="tagline">Stretch ... Strength ... Run</p>
    <div class="divider divider--bottom"></div>

    <p class="philosophy">Any order you like...pick all or one. Only fear holds you back from experiencing any of these. We teach all our classes to what is happening in your body in this moment with an eye for alignment, correct muscle recruitment and breath awareness.</p>
  </section>
</body>
</html>
```